Franchise Vacation Rental Company Website

We are looking for fresh, new and creative design ideas to help enhance this site. We are a vacation rental company that is starting a new franchise business. This will be our home franchise page, and will need to appeal to franchise candidates as well as travelers looking for vacation homes in our current locations.

Business

```html
<!DOCTYPE html>
<html lang="en">
<head>
<meta charset="utf-8">
<title>Harbor Nest – Vacation Rentals &amp; Franchise</title>
<link href="https://fonts.googleapis.com/css2?family=Open+Sans:wght@300;400;600;700&display=swap" rel="stylesheet">
<style>
:root{
  --green:#4bb826;
  --green-dark:#3a9a1c;
  --navy:#2b3990;
  --title:#1f3d7a;
  --header:#3d3d3d;
  --nav:#2f2f2f;
  --text:#555;
  --muted:#777;
  --line:#e3e3e3;
  --footer:#f4f4f4;
}
*{margin:0;padding:0;box-sizing:border-box}
html,body{width:836px;height:1200px;overflow:hidden;background:#fff}
body{font-family:"Open Sans",Arial,sans-serif;color:var(--text);position:relative}
.abs{position:absolute}
.site-header{left:0;top:0;width:836px;height:73px;background:var(--header);border-top:2px solid var(--green)}
.brand{left:129px;top:18px;display:flex;align-items:center;gap:8px;color:var(--green);font-size:29px;font-weight:300;letter-spacing:.5px}
.brand-dot{width:12px;height:12px;border-radius:50%;background:var(--green)}
.contact-top{left:537px;top:14px;display:flex;align-items:center;gap:8px}
.phone-ring{width:38px;height:38px;border:2px solid var(--green);border-radius:50%;display:flex;align-items:center;justify-content:center}
.contact-top .ask{font-size:8.5px;color:var(--green)}
.contact-top .num{font-size:16px;color:#fff;letter-spacing:1px;line-height:1.1}
.contact-top .mail{font-size:10px;color:#eee;letter-spacing:.5px}
.main-nav{left:0;top:73px;width:836px;height:27px;background:var(--nav)}
.main-nav ul{list-style:none;display:flex;position:absolute;left:127px;top:0;height:27px}
.main-nav li{font-size:10px;font-weight:600;color:#fff;padding:0 9.5px;line-height:27px;position:relative}
.main-nav li.active::before{content:"";position:absolute;left:0;right:0;top:0;height:2px;background:#ddd}
.hero{left:0;top:100px;width:836px;height:239px;background:linear-gradient(100deg,#5a5148 0%,#a49a8c 25%,#d8d4cc 55%,#eeece8 80%,#cfcac2 100%)}
.hero-card{left:121px;top:160px;width:340px}
.hero-title{background:rgba(35,55,140,.88);height:32px;padding:0 13px;font-size:18px;font-weight:600;color:var(--green);line-height:32px}
.hero-text{margin-top:7px;background:rgba(35,55,140,.82);padding:9px 13px;font-size:8.5px;color:#fff;line-height:1.75}
.btn{display:inline-block;background:var(--green);color:#fff;font-weight:600;border:1px solid var(--green-dark)}
.hero-btn{left:121px;top:253px;font-size:8.5px;padding:6px 14px}
.finder{left:0;top:339px;width:836px;height:60px;text-align:center;background:linear-gradient(#f6f6f6,#fff);border-bottom:2px solid var(--green)}
.finder h2{font-size:19px;font-weight:400;color:var(--title);margin-top:10px;display:flex;justify-content:center;align-items:center;gap:3px}
.finder h2 em{font-style:normal;color:var(--green)}
.finder p{font-size:9px;color:var(--muted);margin-top:2px}
.finder-notch{left:412px;top:397px;width:10px;height:6px}
.arrow{top:506px}
.card{top:420px;width:139px;height:206px;border:1px solid var(--line);background:#fff}
.card-photo{height:91px}
.price{position:absolute;left:24px;top:75px;width:90px;height:25px;background:var(--green);color:#fff;font-size:10.5px;font-weight:600;text-align:center;line-height:25px}
.card h3{font-size:9.5px;font-weight:600;color:var(--title);margin:20px 0 4px 10px}
.card ul{list-style:none;margin:0 10px}
.card li{font-size:7.5px;color:var(--text);height:20px;display:flex;align-items:center;gap:5px;border-bottom:1px solid #eee}
.card li:last-child{border-bottom:0}
.card li svg{flex:none}
.discover{left:121px;top:665px;width:594px;height:135px;border:1px solid #ececec;background:#fcfcfc;text-align:center}
.discover-banner{left:214px;top:649px;width:408px;height:33px;background:var(--navy);color:#fff;font-size:15px;font-weight:300;text-align:center;line-height:33px;letter-spacing:.3px}
.discover h4{font-size:12.5px;font-weight:600;color:var(--green);margin-top:36px}
.discover p{font-size:8.3px;line-height:1.65;padding:0 12px;margin-top:6px;color:var(--text)}
.discover .btn{font-size:8px;padding:2px 7px;margin-top:8px}
.feature{top:827px;width:170px;text-align:center}
.feature h5{font-size:14.5px;font-weight:400;color:var(--title);margin-top:20px}
.feature p{font-size:8.3px;line-height:1.65;margin-top:8px}
.feature svg{display:block;margin:0 auto}
.divider{top:826px;width:1px;height:168px;background:#e6e6e6}
.site-footer{left:0;top:1031px;width:836px;height:141px;background:var(--footer);border-top:1px solid #eee}
.site-footer h6{font-size:12.5px;font-weight:400;color:var(--green);letter-spacing:.3px}
.f-links{list-style:none;margin-top:9px}
.f-links li{font-size:8.3px;color:var(--muted);height:17.5px}
.f-contact p{font-size:8.3px;color:var(--muted);line-height:1.35;margin-top:6px}
.map{left:554px;top:1081px;width:161px;height:66px;background:linear-gradient(135deg,#9a9a9a,#b7b7b7 60%,#a8a8a8)}
.map span{position:absolute;left:0;right:0;bottom:9px;text-align:center;color:#fff;font-size:10px;font-weight:600;letter-spacing:.5px}
.copyright{left:0;top:1181px;width:836px;text-align:center;font-size:7.5px;color:var(--muted)}
</style>
</head>
<body>

<header class="abs site-header">
  <div class="abs brand"><span>Harbor Nest</span><span class="brand-dot"></span></div>
  <div class="abs contact-top">
    <div class="phone-ring">
      <svg width="18" height="18" viewBox="0 0 24 24"><path d="M6.6 10.8c1.4 2.8 3.8 5.1 6.6 6.6l2.2-2.2c.3-.3.7-.4 1-.2 1.1.4 2.3.6 3.6.6.6 0 1 .4 1 1V20c0 .6-.4 1-1 1C10.6 21 3 13.4 3 4c0-.6.4-1 1-1h3.5c.6 0 1 .4 1 1 0 1.3.2 2.5.6 3.6.1.3 0 .7-.2 1z" fill="#4bb826"/></svg>
    </div>
    <div>
      <div class="ask">Ask Our Experts</div>
      <div class="num">1 (800) 555 0142</div>
      <div class="mail">hello@harbornest-stays.com</div>
    </div>
  </div>
</header>

<nav class="abs main-nav">
  <ul>
    <li class="active">Home</li>
    <li>See our Harbor Nests</li>
    <li>Franchise Informations</li>
    <li>Our Philosophy</li>
    <li>List your Property</li>
    <li>Contact Us</li>
    <li>News</li>
  </ul>
</nav>

<section class="abs hero" role="img" aria-label="Bright white villa living room with sectional sofa and open kitchen"></section>
<div class="abs hero-card">
  <div class="hero-title">Willow Villa</div>
  <div class="hero-text">This is a lovely villa located near the lake Marrow. Sun facing with heated pool would suit all your needs and luxuries.</div>
</div>
<span class="abs btn hero-btn">Know more &gt;&gt;</span>

<section class="abs finder">
  <h2><svg width="12" height="15" viewBox="0 0 12 16"><path d="M6 1a5 5 0 0 0-5 5c0 3.6 5 9 5 9s5-5.4 5-9a5 5 0 0 0-5-5z" fill="none" stroke="#4bb826" stroke-width="1.8"/><circle cx="6" cy="6" r="1.8" fill="#4bb826"/></svg>Find your <em>Harbor Nest!</em></h2>
  <p>Choose one of the locations below to begin your search</p>
</section>
<svg class="abs finder-notch" viewBox="0 0 10 6"><path d="M0 0 L5 5 L10 0" fill="#fff" stroke="#4bb826" stroke-width="1.5"/></svg>

<svg class="abs arrow" style="left:92px" width="16" height="30" viewBox="0 0 16 30"><path d="M14 2 L2 15 L14 28" fill="none" stroke="#2b3990" stroke-width="2"/></svg>
<svg class="abs arrow" style="left:727px" width="16" height="30" viewBox="0 0 16 30"><path d="M2 2 L14 15 L2 28" fill="none" stroke="#2b3990" stroke-width="2"/></svg>

<article class="abs card" style="left:121px">
  <div class="card-photo" role="img" aria-label="Waterfront garden with umbrella and lounge chairs" style="background:linear-gradient(#7aa5d6,#9cc0e0 40%,#5f8f3a 60%,#3f6e2a)"></div>
  <div class="price">$15,000,00</div>
  <h3>Maryland Eastern Shore</h3>
  <ul>
    <li><svg width="9" height="9" viewBox="0 0 10 10"><circle cx="5" cy="5" r="5" fill="#4bb826"/><rect x="4.4" y="4" width="1.4" height="4" fill="#fff"/><circle cx="5.1" cy="2.6" r=".8" fill="#fff"/></svg>Property Id : ABC123</li>
    <li><svg width="10" height="10" viewBox="0 0 10 10"><path d="M5 0l2 2H6v2h2V3l2 2-2 2V6H6v2h1l-2 2-2-2h1V6H2v1L0 5l2-2v1h2V2H3z" fill="#4bb826"/></svg>Area : 4000 Sq. Ft.</li>
    <li><svg width="11" height="8" viewBox="0 0 11 8"><path d="M0 0h1.5v4H11v4H9.5V6.5h-8V8H0zM3 1.5h7V3.5H3z" fill="#4bb826"/></svg>3 Bedroom</li>
    <li><svg width="11" height="10" viewBox="0 0 11 10"><path d="M1 0h2v1H2v4h9v2c0 1-1 2-2 2H3C2 9 1 8 1 7zM3 9l-1 1h1.5zM8 9l1 1H7.5z" fill="#4bb826"/></svg>3 Bathroom</li>
  </ul>
</article>

<article class="abs card" style="left:273px">
  <div class="card-photo" role="img" aria-label="Harbor marina with red-roofed buildings" style="background:linear-gradient(#6f9fd8,#a7c6e6 45%,#7a8a6a 62%,#2d4a6a)"></div>
  <div class="price">$15,000,00</div>
  <h3>St. Michaels, MD</h3>
  <ul>
    <li><svg width="9" height="9" viewBox="0 0 10 10"><circle cx="5" cy="5" r="5" fill="#4bb826"/><rect x="4.4" y="4" width="1.4" height="4" fill="#fff"/><circle cx="5.1" cy="2.6" r=".8" fill="#fff"/></svg>Property Id : ABC123</li>
    <li><svg width="10" height="10" viewBox="0 0 10 10"><path d="M5 0l2 2H6v2h2V3l2 2-2 2V6H6v2h1l-2 2-2-2h1V6H2v1L0 5l2-2v1h2V2H3z" fill="#4bb826"/></svg>Area : 4000 Sq. Ft.</li>
    <li><svg width="11" height="8" viewBox="0 0 11 8"><path d="M0 0h1.5v4H11v4H9.5V6.5h-8V8H0zM3 1.5h7V3.5H3z" fill="#4bb826"/></svg>3 Bedroom</li>
    <li><svg width="11" height="10" viewBox="0 0 11 10"><path d="M1 0h2v1H2v4h9v2c0 1-1 2-2 2H3C2 9 1 8 1 7zM3 9l-1 1h1.5zM8 9l1 1H7.5z" fill="#4bb826"/></svg>3 Bathroom</li>
  </ul>
</article>

<article class="abs card" style="left:425px">
  <div class="card-photo" role="img" aria-label="Tree-lined path beside a white inn with porch" style="background:linear-gradient(100deg,#4d7a2e,#8bb05a 45%,#e6ecef 75%,#c9d4dc)"></div>
  <div class="price">$15,000,00</div>
  <h3>Oxford, MD</h3>
  <ul>
    <li><svg width="9" height="9" viewBox="0 0 10 10"><circle cx="5" cy="5" r="5" fill="#4bb826"/><rect x="4.4" y="4" width="1.4" height="4" fill="#fff"/><circle cx="5.1" cy="2.6" r=".8" fill="#fff"/></svg>Property Id : ABC123</li>
    <li><svg width="10" height="10" viewBox="0 0 10 10"><path d="M5 0l2 2H6v2h2V3l2 2-2 2V6H6v2h1l-2 2-2-2h1V6H2v1L0 5l2-2v1h2V2H3z" fill="#4bb826"/></svg>Area : 4000 Sq. Ft.</li>
    <li><svg width="11" height="8" viewBox="0 0 11 8"><path d="M0 0h1.5v4H11v4H9.5V6.5h-8V8H0zM3 1.5h7V3.5H3z" fill="#4bb826"/></svg>3 Bedroom</li>
    <li><svg width="11" height="10" viewBox="0 0 11 10"><path d="M1 0h2v1H2v4h9v2c0 1-1 2-2 2H3C2 9 1 8 1 7zM3 9l-1 1h1.5zM8 9l1 1H7.5z" fill="#4bb826"/></svg>3 Bathroom</li>
  </ul>
</article>

<article class="abs card" style="left:577px">
  <div class="card-photo" role="img" aria-label="Pier with lighthouse on calm bay waters" style="background:linear-gradient(#3f6fb8,#7ea4d6 55%,#4a5a6a 64%,#223a5a)"></div>
  <div class="price">$15,000,00</div>
  <h3>Cambridge, MD</h3>
  <ul>
    <li><svg width="9" height="9" viewBox="0 0 10 10"><circle cx="5" cy="5" r="5" fill="#4bb826"/><rect x="4.4" y="4" width="1.4" height="4" fill="#fff"/><circle cx="5.1" cy="2.6" r=".8" fill="#fff"/></svg>Property Id : ABC123</li>
    <li><svg width="10" height="10" viewBox="0 0 10 10"><path d="M5 0l2 2H6v2h2V3l2 2-2 2V6H6v2h1l-2 2-2-2h1V6H2v1L0 5l2-2v1h2V2H3z" fill="#4bb826"/></svg>Area : 4000 Sq. Ft.</li>
    <li><svg width="11" height="8" viewBox="0 0 11 8"><path d="M0 0h1.5v4H11v4H9.5V6.5h-8V8H0zM3 1.5h7V3.5H3z" fill="#4bb826"/></svg>3 Bedroom</li>
    <li><svg width="11" height="10" viewBox="0 0 11 10"><path d="M1 0h2v1H2v4h9v2c0 1-1 2-2 2H3C2 9 1 8 1 7zM3 9l-1 1h1.5zM8 9l1 1H7.5z" fill="#4bb826"/></svg>3 Bathroom</li>
  </ul>
</article>

<section class="abs discover">
  <h4>Explore... Experience... Enjoy...</h4>
  <p>Lorem ipsum dolor sit amet, consectetur adipiscing elit. Aliquam rhoncus cursus ipsum, in dignissim tellus volutpat non. Mauris lectus eros, iaculis vitae luctus a, laoreet eget est. In nisl massa, aliquam a mollis ac, ultricies sed lorem. Cras posuere tincidunt massa, a feugiat erat pellentesque ac. Maecenas eu pretium justo. Pellentesque euismod facilisis urna eu mollis.</p>
  <span class="btn">Read More</span>
</section>
<div class="abs discover-banner">READY TO DISCOVER YOUR NEXT HARBOR NEST?</div>

<div class="abs feature" style="left:116px">
  <svg width="58" height="58" viewBox="0 0 58 58"><defs><clipPath id="c1"><circle cx="29" cy="29" r="29"/></clipPath></defs><circle cx="29" cy="29" r="29" fill="#2b3990"/><path d="M29 40 L60 71 L60 20 L40 20z" fill="#1f2a6e" clip-path="url(#c1)"/><path d="M29 13a10 10 0 0 0-10 10c0 7 10 17 10 17s10-10 10-17a10 10 0 0 0-10-10z" fill="#fff"/><circle cx="29" cy="23" r="4.5" fill="#2b3990"/></svg>
  <h5>Know of a Harbor Nest?</h5>
  <p>Lorem ipsum dolor sit amet, consectetur adipiscing elit. Aliquam rhoncus cursus ipsum, in dignissim tellus volutpat non. Mauris lectus eros, iaculis vitae luctus a, laoreet eget est.</p>
</div>
<div class="abs divider" style="left:310px"></div>
<div class="abs feature" style="left:333px">
  <svg width="58" height="58" viewBox="0 0 58 58"><defs><clipPath id="c2"><circle cx="29" cy="29" r="29"/></clipPath></defs><circle cx="29" cy="29" r="29" fill="#2b3990"/><path d="M26 42 L58 74 L58 30 L40 16z" fill="#1f2a6e" clip-path="url(#c2)"/><path d="M32 14 L42 14 L42 24 L28 38 L18 28z" fill="#fff"/><circle cx="37" cy="19" r="2" fill="#2b3990"/></svg>
  <h5>Spot Travel Free!</h5>
  <p>Lorem ipsum dolor sit amet, consectetur adipiscing elit. Aliquam rhoncus cursus ipsum, in dignissim tellus volutpat non. Mauris lectus eros, iaculis vitae luctus a, laoreet eget est.</p>
</div>
<div class="abs divider" style="left:527px"></div>
<div class="abs feature" style="left:548px">
  <svg width="58" height="58" viewBox="0 0 58 58"><defs><clipPath id="c3"><circle cx="29" cy="29" r="29"/></clipPath></defs><circle cx="29" cy="29" r="29" fill="#2b3990"/><path d="M38 38 L66 66 L66 20 L40 20z" fill="#1f2a6e" clip-path="url(#c3)"/><circle cx="29" cy="29" r="13" fill="#fff"/><circle cx="29" cy="29" r="10" fill="#2b3990"/><path d="M29 22 V29 H35" fill="none" stroke="#fff" stroke-width="2.4"/></svg>
  <h5>Last Minute Deals</h5>
  <p>Lorem ipsum dolor sit amet, consectetur adipiscing elit. Aliquam rhoncus cursus ipsum, in dignissim tellus volutpat non. Mauris lectus eros, iaculis vitae luctus a, laoreet eget est.</p>
</div>

<footer class="abs site-footer">
  <div class="abs" style="left:121px;top:22px">
    <h6>USEFUL LINKS</h6>
    <ul class="f-links">
      <li>About Harbor Nest</li>
      <li>Why a Harbor Nest Franchise</li>
      <li>Frequently Asked Questions</li>
      <li>Our Philosophy</li>
    </ul>
  </div>
  <div class="abs" style="left:277px;top:41px">
    <ul class="f-links">
      <li>List your Properties</li>
      <li>Contact Us</li>
      <li>Site Map</li>
      <li>Privacy Policy</li>
    </ul>
  </div>
  <div class="abs f-contact" style="left:403px;top:22px">
    <h6>CONTACT INFO</h6>
    <p>48, W, Linden Lane,<br>Easton, MD, 21601</p>
    <p>1.844.555.NEST<br>(1.844.555.6378)</p>
    <p>info@harbornest-stays.com</p>
  </div>
  <div class="abs" style="left:554px;top:22px">
    <h6>LOCATION MAP</h6>
  </div>
</footer>
<div class="abs map" role="img" aria-label="Street map of the Easton office location">
  <svg class="abs" style="left:69px;top:7px" width="24" height="32" viewBox="0 0 24 32"><path d="M12 1a11 11 0 0 0-11 11c0 8 11 19 11 19s11-11 11-19A11 11 0 0 0 12 1z" fill="#fff"/><circle cx="12" cy="12" r="5" fill="#a8a8a8"/></svg>
  <span>VIEW MAP</span>
</div>
<div class="abs copyright">Copyright © 2014 Harbor Nest</div>

</body>
</html>
```